Real estate company needs a letterhead design

A young real estate company needs a letterhead / stationery design, it should include the company's logo. It should look exactly the same as on the business cards. (With the phrase "a brand of KEV Wohnbau & Grundstücksentwicklung GmbH")

In addition, it should also include the 4 round seals.

color code blue # 00456b gray # 333333

Word and PDF are welcome.

KEV Wohnbau & Grundstücksentwicklung GmbH
Managing director: Mag. Lukas Fellnhuber
Matthias-Ortner-Strasse 3c / 41
6300 Wörgl

Tel .: +436648172093
Email: office@wohnglanz-beispiel.at
Web: www.wohnglanz-beispiel.at

Sparkasse Almtal, Bergländer Sparkasse from 1882, Genossenschaftskasse
Anton-Weissauer-Strasse 7, 6300 Wörgl
IBAN: AT31 4817 2964 0058 2316
BIC: GLMTAT44XXX
Account holder: KEV Wohnbau & Grundstücksentwicklung GmbH

FN: XXXXXXX
UID: XXXXXXX

```html
<!DOCTYPE html>
<html lang="de">
<head>
<meta charset="utf-8">
<title>Wohnglanz Letterhead</title>
<link rel="stylesheet" href="https://fonts.googleapis.com/css2?family=Arimo:wght@400;700&family=Montserrat:wght@300;400&family=Open+Sans:wght@400;700&display=swap">
<style>
  :root {
    --brand-blue: #00456b;
    --ink: #333333;
    --body-grey: #9a9a9a;
    --meta-grey: #8a8a8a;
    --rule: #333333;
    --backdrop: #dfe6ee;
    --paper: #ffffff;
  }
  * { margin: 0; padding: 0; box-sizing: border-box; }
  html, body { width: 1200px; height: 1200px; overflow: hidden; background: var(--backdrop); }
  .letterhead {
    position: absolute; left: 176px; top: 0;
    width: 848px; height: 1200px; background: var(--paper);
    font-family: "Arimo", Arial, sans-serif; color: var(--ink);
  }
  .brand { position: absolute; left: 52px; top: 52px; }
  .brand-name {
    display: flex; align-items: center; gap: 10px;
    font-family: "Open Sans", sans-serif; font-weight: 700;
    font-size: 46px; line-height: 1; color: var(--brand-blue); letter-spacing: 1px;
  }
  .brand-dot { width: 14px; height: 14px; background: var(--brand-blue); }
  .brand-tagline {
    font-family: "Open Sans", sans-serif; font-size: 9.5px;
    color: var(--ink); margin-top: 8px;
  }
  .company-data {
    position: absolute; left: 398px; top: 33px;
    font-size: 14px; line-height: 17px;
  }
  .company-data .gap { height: 6px; }
  .company-data b { color: var(--brand-blue); }
  .header-rule { position: absolute; left: 52px; top: 130px; width: 742px; height: 2px; background: var(--rule); }

  .letter { font-family: "Montserrat", sans-serif; font-weight: 300; }
  .recipient { position: absolute; left: 87px; top: 268px; }
  .recipient-label { font-size: 14px; letter-spacing: 2px; color: var(--ink); font-weight: 400; }
  .recipient-name { font-size: 14px; color: var(--brand-blue); font-weight: 400; margin-top: 8px; }
  .recipient-address { font-size: 11px; line-height: 19px; color: var(--meta-grey); margin-top: 5px; }
  .letter-date { position: absolute; right: 86px; top: 266px; font-size: 11.5px; color: var(--ink); font-weight: 400; }

  .letter-body {
    position: absolute; left: 87px; top: 428px; width: 675px;
    font-size: 11.6px; line-height: 15px; color: var(--body-grey); text-align: justify;
  }
  .letter-body p { margin-bottom: 15px; }

  .signature-mark {
    position: absolute; left: 87px; top: 842px; width: 146px; height: 40px;
    background: linear-gradient(90deg, #f1f1f1, #e4e4e4);
  }
  .signatory { position: absolute; left: 85px; top: 889px; }
  .signatory-name { font-size: 13.5px; font-weight: 400; color: var(--ink); letter-spacing: .5px; }
  .signatory-role { font-size: 11px; color: var(--meta-grey); margin-top: 2px; }

  .footer { position: absolute; left: 43px; top: 1096px; display: flex; font-size: 14px; line-height: 17px; }
  .footer-col { padding-right: 18px; }
  .footer-col + .footer-col { border-left: 1px solid var(--ink); padding-left: 16px; }
  .footer-col.contact { padding-top: 17px; }
  .footer-col.bank { padding-top: 17px; }
  .footer-col b { color: var(--brand-blue); }
</style>
</head>
<body>
<main class="letterhead">
  <header>
    <div class="brand">
      <div class="brand-name">WOHNGLANZ <span class="brand-dot"></span></div>
      <div class="brand-tagline">eine Marke der KEV Wohnbau &amp; Grundstücksentwicklung GmbH</div>
    </div>
    <div class="company-data">
      <div><b>FN:</b> XXXXXXX</div>
      <div><b>UID:</b> XXXXXXX</div>
      <div class="gap"></div>
      <div><b>IBAN:</b> AT31 4817 2964 0058 2316</div>
      <div><b>BIC:</b> GLMTAT44XXX</div>
      <div><b>Account holder:</b> KEV Wohnbau &amp; Grundstücksentwicklung GmbH</div>
    </div>
    <div class="header-rule"></div>
  </header>

  <section class="letter">
    <div class="recipient">
      <div class="recipient-label">TO</div>
      <div class="recipient-name">Tobias Lanzinger</div>
      <div class="recipient-address">Human Resources<br>Nordhang Systems Inc.<br>2207-B Lindenweg, Halden<br>E41 USA</div>
    </div>
    <div class="letter-date">Friday, 01/01/2018</div>

    <div class="letter-body">
      <p>Lorem ipsum dolor sit amet, consectetuer adipiscing elit, sed diam nonmmy nibh euismod tincidunt ut laoreet dolore magna aliquam erat volutpat. Ut wisi enim ad minim veniam, quis nostrud exerci tationmcorper suscipit lobortis nisl ut aliquip ex ea commodo consequat. Duis autem vel eum iriure dolor in hendrerit in vulputate velit esse molestie consequat, vel illum dolore eu feugiat nulla facilisis at vero eros et accumsan et iusto odio dignissim qui blandit praesent luptatum zzril delenit augue duis dolore te feugait nulla facilisi.</p>
      <p>Nam liber tempor cum soluta nobis eleifend option congue nihil imprdiet doming id quod mazim placerat facer possim assum. Typi non habent claritatem insitam;</p>
      <p>Est usus legentis in iis qui facit eorum claritatem.</p>
      <p>Investigationes demonstraverunt lectores legere me lius quod ii legunt saepius. Claritas est etiam processus dynamicus, qui sequitur mutationem consuetudium lectorum. Mirum est notare quam littera gothica, quam nunc putamus parum claram, anteposuerit litterarum formas humanitatis per seacula quarta decima et quinta decima. Eodem modo typi, qui nunc nobis videntur parum clari, fiant sollemnes in futurum.</p>
      <p>consectetuer adipiscing elit, sed diam nonummy nibh euismod tincidunt ut laoreet dolore magna aliquam erat volutpat. Ut wisi enim ad minim veniam, quis nostrud exerci tation ullamcorper suscipit lobortis nisl ut aliquip ex ea commodo consequat. Duis autem vel eum iriure dolor in hendrerit in vulputate velit esse molestie consequat, vel illum dolore eu feugiat nulla facilisis at vero eros et accumsan et iusto odio dignissim qui blandit praesent luptatum zzril delenit augue duis dolore te feugait nulla facilisi.</p>
      <p>Nam liber tempor cum soluta nobis eleifend option congue nihil imperdiet .</p>
    </div>

    <div class="signature-mark" role="img" aria-label="Handwritten signature of Peter Haslauer"></div>
    <div class="signatory">
      <div class="signatory-name">Peter Haslauer</div>
      <div class="signatory-role">Managing Director</div>
    </div>
  </section>

  <footer class="footer">
    <div class="footer-col">
      <b>Mag. Lukas Fellnhuber</b><br>Managing director<br>Matthias-Ortner-Strasse 3c / 41<br>6300 Wörgl
    </div>
    <div class="footer-col contact">
      Tel .: +436648172093<br>Email: office@wohnglanz-beispiel.at<br>Web: www.wohnglanz-beispiel.at
    </div>
    <div class="footer-col bank">
      Sparkasse Almtal<br>Bergländer Sparkasse from 1882, Genossenschaftskasse<br>Anton-Weissauer-Strasse 7, 6300 Wörgl
    </div>
  </footer>
</main>
</body>
</html>
```